FenderPals Personal Injury Lawyers Website (Wordpress)

We need a brand new website for our firm's new rebranding. The name of the website is www.fenderpals-example.com. Our new brand will be a group of personal injury lawyers focused on representing only victims in car wrecks. We will be distinguishing ourselves from other law firms due to the fact that other law firms represent clients involving all forms of personal injury. We will only focus on car wrecks and this needs to be reflected on the website.

I have attached the new firm logo and stationary to show the designers the kind of look we are going for in the new website. It needs to be clean, pure, and show the potential clients that we only do one thing and we do it well. That thing is car wrecks.

Some examples of websites that we like are the following:
www.qvt-example.lu - nice interface and colors. nice navigation, we really like the biography pages for the individuals attorneys
www.morvantlegal-example.com - good layout, good navigation
www.pelliardwoss-example.com - navigation bar follows the user whether the user goes up or down

We would like five separate pages -- (1) Home, (2) Client Resources, (3) Expertise / Car Wrecks, (4) Contact Us, (5) News

The Home page will be used for driving traffic and should have a call to action on the right at the top stating that we will send an ebook to anyone who gives their contact information. The ebook will explain how car wrecks work. This should also have room for youtube videos which will be added later.

The client resources will include blogs, books, and information for potential clients. It should be presented in a well developed manner which is both appealing to potential and current clients.

The expertise page will show that we only focus on car wrecks. This needs to be a recurrent theme throughout the entire website. This page will focus on car wrecks and the different aspects including damages, insurance, and investigation.

The Contact Us page will show a google map to our address and phone number. Please use generic information and we will fill in the gaps upon the selection.

News: the news page will show different articles related to past and present cases and the successes of those clients.

The overall page should be elegant and creative. Do not include courthouses, gavels or anything else related to the law. If you include these things, your design will automatically be excluded.
Updates

Please take note this design is now guaranteed. I look forward to receiving everyone's wonderful designs.

Target Market(s)

Persons involved in car wrecks

Industry/Entity Type

Legal

Coding

Coded - Design and coding required

Number of Pages Required

5+ page

Font styles to use
Serif
Sans Serif

Colors
ec1f27
ffffff
000000

Requirements
Must have
• Five pages which focus on representation of car wreck victims. The site must be clean and easy to navigate.
Nice to have
• Navigation bar should follow user up and down the page.
Should not have
• Gavels, court houses, anything related to the law. If your design has these aspects, it will automatically be rejected

```html
<!DOCTYPE html>
<html lang="en">
<head>
<meta charset="utf-8">
<title>FenderPals – Personal Injury Lawyers</title>
<link rel="stylesheet" href="https://fonts.googleapis.com/css2?family=Roboto+Condensed:wght@400;700&family=Open+Sans:wght@400;600&display=swap">
<style>
:root{
  --red:#ec1f27;
  --red-dark:#b8141a;
  --ink:#111111;
  --dark:#1b1b1b;
  --dark-2:#2a2a2a;
  --grey:#6f6f6f;
  --grey-light:#d9d9d9;
  --paper:#ffffff;
  --soft:#f3f3f3;
}
*{box-sizing:border-box;margin:0;padding:0}
html,body{width:1200px;height:2244px;overflow:hidden}
body{background:var(--paper);font-family:"Open Sans",Arial,sans-serif;color:var(--grey);font-size:13px;line-height:1.6}
.head{font-family:"Roboto Condensed","Arial Narrow",sans-serif;font-weight:700;text-transform:uppercase;color:var(--ink)}
.accent{color:var(--red)}

/* header */
.site-header{height:120px;position:relative;padding:0 100px}
.brand{position:absolute;left:100px;top:22px}
.brand-name{font-family:"Roboto Condensed",sans-serif;font-weight:700;font-size:50px;line-height:1;color:var(--ink);letter-spacing:1px}
.brand-tag{font-family:"Roboto Condensed",sans-serif;font-size:15px;color:var(--red);letter-spacing:2px;margin-top:4px}
.ebook-cta{position:absolute;right:100px;top:32px;height:46px;display:flex}
.ebook-cta .icon{width:56px;background:var(--dark);display:flex;align-items:center;justify-content:center;clip-path:polygon(14px 0,100% 0,100% 100%,0 100%)}
.ebook-cta .label{background:var(--red);color:#fff;font-family:"Roboto Condensed",sans-serif;font-weight:700;font-size:16px;display:flex;align-items:center;padding:0 22px;letter-spacing:.5px}

/* nav */
.main-nav{height:40px;background:var(--dark);display:flex;padding:0 100px}
.main-nav a,.foot-nav a{font-family:"Roboto Condensed",sans-serif;font-weight:700;font-size:13px;text-transform:uppercase;text-decoration:none;letter-spacing:.5px}
.main-nav a{color:#fff;flex:1;display:flex;align-items:center;justify-content:center}
.main-nav a.current{background:var(--red);flex:0 0 140px}

/* hero */
.hero{height:480px;position:relative;overflow:hidden}
.hero-photo{position:absolute;inset:0;background:radial-gradient(ellipse at 72% 55%,#b3161c 0%,#6a0c10 28%,#1d1d1f 60%,#0c0c0d 100%)}
.hero-copy{position:absolute;left:100px;top:190px;width:440px}
.hero-copy h1{font-family:"Roboto Condensed",sans-serif;font-weight:700;color:#fff;font-size:36px;line-height:1.05;text-transform:uppercase}
.hero-copy .sub{color:var(--red);font-size:14px;margin:8px 0 10px;font-weight:600}
.hero-copy p{color:#c9c9c9;font-size:12px;line-height:1.5}
.btn{display:inline-flex;height:40px;margin-top:22px;text-decoration:none}
.btn .txt{background:var(--red);color:#fff;font-family:"Roboto Condensed",sans-serif;font-weight:700;font-size:13px;padding:0 18px 0 26px;display:flex;align-items:center;clip-path:polygon(14px 0,100% 0,100% 100%,0 100%)}
.btn .arr{width:44px;background:var(--ink);display:flex;align-items:center;justify-content:center;clip-path:polygon(0 0,100% 0,calc(100% - 14px) 100%,0 100%);margin-left:-1px}

/* welcome */
.welcome{height:530px;padding:80px 100px 0;display:flex;gap:60px}
.welcome-text{width:440px}
.welcome-text .pre{font-family:"Roboto Condensed",sans-serif;font-size:26px;color:var(--grey);line-height:1}
.welcome-text h2{font-size:52px;line-height:1.05;margin-bottom:16px}
.welcome-text p{font-size:12.5px;margin-bottom:14px}
.video-block{flex:1}
.video-block h2{font-size:26px;line-height:1.1}
.video-block .cap{font-size:12px;margin:4px 0 12px}
.video-frame{height:290px;position:relative;background:linear-gradient(160deg,#e9e9e9 0%,#c6c6c6 40%,#7d7d7d 75%,#3a3a3a 100%)}
.video-frame svg{position:absolute;left:50%;top:50%;transform:translate(-50%,-50%)}

/* why & news */
.columns{height:620px;padding:30px 100px 0;display:flex;gap:60px}
.col{width:470px}
.col-title{font-size:26px;padding-bottom:10px;border-bottom:1px solid var(--grey-light);margin-bottom:26px;position:relative}
.col-title::after{content:"";position:absolute;left:0;bottom:-1px;width:70px;height:3px;background:var(--red)}
.acc-item{height:50px;display:flex;align-items:center;border:1px solid var(--grey-light);margin-bottom:14px}
.acc-item .ico{width:56px;height:100%;display:flex;align-items:center;justify-content:center;background:var(--soft);clip-path:polygon(0 0,100% 0,calc(100% - 12px) 100%,0 100%)}
.acc-item .name{font-family:"Roboto Condensed",sans-serif;font-weight:700;font-size:14px;color:var(--ink);text-transform:uppercase;padding-left:20px}
.acc-item.open{background:var(--dark);border-color:var(--dark);margin-bottom:0}
.acc-item.open .ico{background:var(--red)}
.acc-item.open .name{color:#fff}
.acc-body{border:1px solid var(--grey-light);border-top:0;padding:20px 24px 24px;margin-bottom:18px;font-size:12.5px}
.acc-body .btn{margin-top:14px;float:right}
.acc-body::after{content:"";display:block;clear:both}
.news-item{display:flex;gap:18px;margin-bottom:26px}
.news-thumb{width:130px;height:110px;flex:none}
.t1{background:linear-gradient(135deg,#8d8d8d,#3b3b3b 60%,#1c1c1c)}
.t2{background:linear-gradient(135deg,#d3d3d3,#8a1a1d 55%,#2b2b2b)}
.t3{background:linear-gradient(135deg,#5f7590,#2a3140 55%,#121418)}
.news-item h3{font-family:"Roboto Condensed",sans-serif;font-weight:700;font-size:16px;color:var(--red);text-transform:uppercase;line-height:1.2}
.meta{display:flex;gap:16px;font-size:11px;color:var(--grey);margin:4px 0}
.meta span{display:flex;align-items:center;gap:5px}
.news-item p{font-size:12px;line-height:1.5}
.more{color:var(--red);font-size:12px;font-weight:600}

/* contact footer */
.contact{height:330px;background:var(--dark);padding:50px 100px 0;display:flex;gap:60px}
.contact-form{width:620px}
.contact h2{font-size:26px;color:#fff;margin-bottom:22px}
.fields{display:grid;grid-template-columns:1fr 1fr;gap:16px 20px}
.field{height:40px;background:#fff;font-size:12px;color:#888;padding:0 14px;display:flex;align-items:center}
.form-foot{display:flex;justify-content:flex-end}
.details{flex:1}
.details li{list-style:none;display:flex;gap:12px;color:#c9c9c9;font-size:12.5px;margin-bottom:10px;align-items:flex-start}
.details svg{flex:none;margin-top:3px}

/* bottom nav */
.foot-nav{height:60px;border-bottom:1px solid var(--grey-light);display:flex;align-items:center;padding:0 100px}
.foot-nav a{color:var(--ink);margin-right:70px}
.socials{margin-left:auto;display:flex;gap:6px}
.socials span{width:34px;height:34px;background:#1f6fb8}
.socials span:last-child{background:var(--red)}
.copy{height:64px;display:flex;align-items:center;padding:0 100px;font-size:11.5px;color:var(--grey)}
</style>
</head>
<body>

<header class="site-header">
  <div class="brand">
    <div class="brand-name">FENDERPALS</div>
    <div class="brand-tag">PERSONAL INJURY LAWYERS</div>
  </div>
  <a class="ebook-cta" href="#">
    <span class="icon"><svg width="20" height="16" viewBox="0 0 20 16"><rect x="1" y="1" width="18" height="14" fill="none" stroke="#fff" stroke-width="2"/><path d="M1 1l9 7 9-7" fill="none" stroke="#fff" stroke-width="2"/></svg></span>
    <span class="label">SEND AN EBOOK</span>
  </a>
</header>

<nav class="main-nav">
  <a class="current" href="#">Home</a>
  <a href="#">Client Resources</a>
  <a href="#">Expertise and Car Wrecks</a>
  <a href="#">Contact Us</a>
  <a href="#">News</a>
</nav>

<section class="hero">
  <div class="hero-photo" role="img" aria-label="Photo of a crashed red car with shattered glass against a dark background"></div>
  <div class="hero-copy">
    <h1>We are FenderPals<br>Lorem dummy test</h1>
    <div class="sub">Lorem ipsum is simply dummy</div>
    <p>Lorem ipsum is simply dummy text of the printing and typesetting industry. It has survived not only five centuries, but also the leap into electronic typesetting, remaining essentially unchanged.</p>
    <a class="btn" href="#"><span class="txt">READ MORE</span><span class="arr"><svg width="12" height="12" viewBox="0 0 12 12"><path d="M3 1l5 5-5 5" fill="none" stroke="#fff" stroke-width="2"/></svg></span></a>
  </div>
</section>

<section class="welcome">
  <div class="welcome-text">
    <div class="pre">Welcome to</div>
    <h2 class="head">FenderPals</h2>
    <p>Lorem ipsum is simply dummy text of the printing and typesetting industry. Lorem ipsum has been the industry's standard dummy text ever since the 1500s, when an unknown printer took a galley of type and scrambled it to make a type specimen book. It has survived not only five centuries, but also the leap into electronic typesetting, remaining essentially unchanged.</p>
    <p>It was popularised in the 1960s with the release of Letraset sheets containing Lorem Ipsum passages, and more recently with desktop publishing software like Aldus PageMaker including versions of Lorem Ipsum.</p>
    <a class="btn" href="#" style="margin-top:8px"><span class="txt">READ MORE</span><span class="arr"><svg width="12" height="12" viewBox="0 0 12 12"><path d="M3 1l5 5-5 5" fill="none" stroke="#fff" stroke-width="2"/></svg></span></a>
  </div>
  <div class="video-block">
    <h2 class="head"><span class="accent">Use video to show how</span> awesome is!</h2>
    <div class="cap">Lorem ipsum is simply dummy text of the printing and typesetting industry.</div>
    <div class="video-frame" role="img" aria-label="Video still of a motorcycle lying on its side after a crash">
      <svg width="70" height="70" viewBox="0 0 70 70"><circle cx="35" cy="35" r="35" fill="#ec1f27"/><path d="M27 21l24 14-24 14z" fill="#fff"/></svg>
    </div>
  </div>
</section>

<section class="columns">
  <div class="col">
    <h2 class="head col-title">Why <span class="accent">choose us</span></h2>
    <div class="acc-item open"><span class="ico"><svg width="16" height="16" viewBox="0 0 16 16"><circle cx="8" cy="8" r="7" fill="#fff"/><path d="M6 4l4 4-4 4" fill="none" stroke="#ec1f27" stroke-width="2"/></svg></span><span class="name">Quality commitment</span></div>
    <div class="acc-body">
      Lorem ipsum is simply dummy text of the printing and typesetting industry. Lorem ipsum has been the industry's standard dummy text ever since the 1500s, when an unknown printer took a galley of type and scrambled it to make a type specimen book.
      <a class="btn" href="#"><span class="txt">READ MORE</span><span class="arr"><svg width="12" height="12" viewBox="0 0 12 12"><path d="M3 1l5 5-5 5" fill="none" stroke="#fff" stroke-width="2"/></svg></span></a>
    </div>
    <div class="acc-item"><span class="ico"><svg width="16" height="16" viewBox="0 0 16 16"><circle cx="8" cy="8" r="7" fill="#999"/><path d="M6 4l4 4-4 4" fill="none" stroke="#fff" stroke-width="2"/></svg></span><span class="name">Quality commitment</span></div>
    <div class="acc-item"><span class="ico"><svg width="16" height="16" viewBox="0 0 16 16"><circle cx="8" cy="8" r="7" fill="#999"/><path d="M6 4l4 4-4 4" fill="none" stroke="#fff" stroke-width="2"/></svg></span><span class="name">Quality commitment</span></div>
    <div class="acc-item"><span class="ico"><svg width="16" height="16" viewBox="0 0 16 16"><circle cx="8" cy="8" r="7" fill="#999"/><path d="M6 4l4 4-4 4" fill="none" stroke="#fff" stroke-width="2"/></svg></span><span class="name">Quality commitment</span></div>
  </div>

  <div class="col">
    <h2 class="head col-title">Recent <span class="accent">news</span></h2>
    <article class="news-item">
      <div class="news-thumb t1" role="img" aria-label="Photo of a wrecked car on a road"></div>
      <div>
        <h3>Lorem ipsum is simply dummy text</h3>
        <div class="meta"><span><svg width="10" height="10"><circle cx="5" cy="3" r="2.5" fill="#ec1f27"/><rect x="1" y="6" width="8" height="4" fill="#ec1f27"/></svg>Admin</span><span><svg width="10" height="10"><rect x="0.5" y="1.5" width="9" height="8" fill="none" stroke="#ec1f27"/></svg>23 June 2015</span><span><svg width="10" height="10"><rect y="1" width="10" height="6" fill="#333"/><path d="M2 7v3l3-3" fill="#333"/></svg>5 Comments</span></div>
        <p>Lorem ipsum is simply dummy text of the printing and typesetting industry. Lorem ipsum has been.</p>
        <span class="more">Read More »</span>
      </div>
    </article>
    <article class="news-item">
      <div class="news-thumb t2" role="img" aria-label="Photo of a damaged red car after a collision"></div>
      <div>
        <h3>Lorem ipsum is simply dummy text</h3>
        <div class="meta"><span><svg width="10" height="10"><circle cx="5" cy="3" r="2.5" fill="#ec1f27"/><rect x="1" y="6" width="8" height="4" fill="#ec1f27"/></svg>Admin</span><span><svg width="10" height="10"><rect x="0.5" y="1.5" width="9" height="8" fill="none" stroke="#ec1f27"/></svg>23 June 2015</span><span><svg width="10" height="10"><rect y="1" width="10" height="6" fill="#333"/><path d="M2 7v3l3-3" fill="#333"/></svg>5 Comments</span></div>
        <p>Lorem ipsum is simply dummy text of the printing and typesetting industry. Lorem ipsum has been.</p>
        <span class="more">Read More »</span>
      </div>
    </article>
    <article class="news-item">
      <div class="news-thumb t3" role="img" aria-label="Photo of a crashed dark blue car at night"></div>
      <div>
        <h3>Lorem ipsum is simply dummy text</h3>
        <div class="meta"><span><svg width="10" height="10"><circle cx="5" cy="3" r="2.5" fill="#ec1f27"/><rect x="1" y="6" width="8" height="4" fill="#ec1f27"/></svg>Admin</span><span><svg width="10" height="10"><rect x="0.5" y="1.5" width="9" height="8" fill="none" stroke="#ec1f27"/></svg>23 June 2015</span><span><svg width="10" height="10"><rect y="1" width="10" height="6" fill="#333"/><path d="M2 7v3l3-3" fill="#333"/></svg>5 Comments</span></div>
        <p>Lorem ipsum is simply dummy text of the printing and typesetting industry. Lorem ipsum has been.</p>
        <span class="more">Read More »</span>
      </div>
    </article>
  </div>
</section>

<section class="contact">
  <div class="contact-form">
    <h2 class="head">Contact us <span class="accent">today!</span></h2>
    <div class="fields">
      <div class="field">Name</div>
      <div class="field">Email</div>
      <div class="field">Phone Number</div>
      <div class="field">Message</div>
    </div>
    <div class="form-foot">
      <a class="btn" href="#"><span class="txt">SUBMIT</span><span class="arr"><svg width="12" height="12" viewBox="0 0 12 12"><path d="M3 1l5 5-5 5" fill="none" stroke="#fff" stroke-width="2"/></svg></span></a>
    </div>
  </div>
  <div class="details">
    <h2 class="head">Contact <span class="accent">details</span></h2>
    <ul>
      <li><svg width="12" height="14" viewBox="0 0 12 14"><path d="M6 0a5 5 0 0 1 5 5c0 4-5 9-5 9S1 9 1 5a5 5 0 0 1 5-5z" fill="#ec1f27"/><circle cx="6" cy="5" r="2" fill="#1b1b1b"/></svg><span>48 Lindale Crossing, Suite 210<br>Carverton, Tennessee 37000</span></li>
      <li><svg width="12" height="12" viewBox="0 0 12 12"><path d="M2 0h3l1 3-2 1.5a7 7 0 0 0 3.5 3.5L9 6l3 1v3a2 2 0 0 1-2 2A10 10 0 0 1 0 2a2 2 0 0 1 2-2z" fill="#ec1f27"/></svg><span>(000) 555-0142</span></li>
      <li><svg width="12" height="12" viewBox="0 0 12 12"><rect x="2" y="0" width="8" height="4" fill="#ec1f27"/><rect x="0" y="4" width="12" height="6" fill="#ec1f27"/><rect x="2" y="8" width="8" height="4" fill="#fff"/></svg><span>(000) 555-0187</span></li>
      <li><svg width="12" height="10" viewBox="0 0 12 10"><rect width="12" height="10" fill="#ec1f27"/><path d="M0 0l6 5 6-5" fill="none" stroke="#1b1b1b"/></svg><span>info@fenderpals-example.com</span></li>
    </ul>
  </div>
</section>

<nav class="foot-nav">
  <a href="#">Home</a>
  <a href="#">Client Resources</a>
  <a href="#">Expertise and Car Wrecks</a>
  <a href="#">Contact Us</a>
  <a href="#">News</a>
  <div class="socials"><span></span><span></span><span></span></div>
</nav>

<div class="copy">FenderPals © 2015 · Copyrights. All Rights Reserved</div>

</body>
</html>
```